Etiketten für Gin
Zielgruppe
Wir sind eine kleine neue Brennerei im bayerischen Oberland und werden unter den Namen „Silver Kite“ und „Silver Kite Lemon“ zwei GIN-Sorten auf den Markt bringen.
Der GIN wird online und vor Ort verkauft und sollte daher eine exklusiv-auffällige Optik haben um die Kunden zu beeindrucken. Zielkunden sind anspruchsvolle Genießer, welche die bayerische Gastlichkeit und Lebenskultur schätzen.
Neu an den beiden Gins ist, dass sie mit Blütenpollen destilliert werden, was auf dem Etikett erscheinen muss.
Aufgabenstellung
Wir suchen zwei sich ähnelnde GIN-Etiketten deren Design ausdrückt, dass es sich um handgemachte und hochwertige GIN handelt, deren Zutat Blütenpollen bisher einzigartig ist.
Statt der oft üblichen Bezeichnung „London Dry Gin“ soll „Halmberg Dry Gin“ und „handcrafted“ auf dem Etikett erscheinen, zusätzlich natürlich die verkehrsüblichen Angaben.
Abgefüllt wird in weißen 500ml Flaschen Typ Vendu mit Korkverschluss von kapselix.com.
Sinnvoll halten wir ein Frontetikett, lassen aber gerne auch andere Vorschläge zu.

```html
<!DOCTYPE html>
<html lang="de">
<head>
<meta charset="utf-8">
<title>Halmberg Dry Gin – Etikett</title>
<link rel="stylesheet" href="https://fonts.googleapis.com/css2?family=Archivo:wght@800&family=Open+Sans:wght@400&display=swap">
<style>
  :root {
    --page: #fafafa;
    --label-light: #f3f3f3;
    --label-mid: #e2e2e2;
    --night: #2b2a29;
    --gold-dark: #7a4a1e;
    --gold: #d4a22a;
    --gold-warm: #c9962e;
    --copper: #a0612a;
    --rust: #7a2e24;
    --white: #ffffff;
  }
  * { margin: 0; padding: 0; box-sizing: border-box; }
  html, body {
    width: 669px; height: 1200px; overflow: hidden;
    background: var(--page);
  }
  .label {
    position: absolute; left: 0; top: 330px;
    width: 669px; height: 541px;
    background: linear-gradient(180deg, var(--label-mid), var(--label-light) 40%, var(--label-mid));
    border-top: 1px dotted #bdbdbd;
    border-bottom: 1px dotted #bdbdbd;
    overflow: hidden;
  }
  .title {
    position: absolute; left: 145px; top: 26px;
    font-family: "Archivo", sans-serif; font-weight: 800;
    font-size: 60px; line-height: 71px; letter-spacing: 0.5px;
    background: linear-gradient(90deg, var(--gold-dark), var(--gold) 25%, var(--gold-warm) 70%, var(--copper));
    -webkit-background-clip: text; background-clip: text;
    color: transparent;
  }
  .title span { display: block; }
  .mountains {
    position: absolute; left: 0; top: 226px;
    width: 669px; height: 315px;
    background: linear-gradient(180deg, rgba(43,42,41,0) 0%, #9a9a9a 22%, #5a5959 40%, var(--night) 58%);
  }
  .brand-block {
    position: absolute; left: 148px; top: 438px;
    font-family: "Open Sans", sans-serif; color: var(--white);
  }
  .brand {
    position: absolute; left: 0; top: 34px;
    font-family: "Archivo", sans-serif; font-weight: 800;
    font-size: 21px; letter-spacing: 0.2px; white-space: nowrap;
  }
  .brand-dot {
    position: absolute; left: 164px; top: 48px;
    width: 5px; height: 5px; border-radius: 50%; background: var(--white);
  }
  .claim {
    position: absolute; left: 172px; top: 0;
    font-size: 15px; line-height: 20px; white-space: nowrap;
  }
  .claim .pollen {
    display: inline-block; margin-top: 2px; padding: 0 1px;
    background: linear-gradient(90deg, var(--gold-dark), var(--gold) 30%, var(--copper) 75%, var(--rust));
  }
  .claim .volume { display: block; margin-top: 4px; padding-left: 1px; }
</style>
</head>
<body>
  <div class="label">
    <h1 class="title"><span>HALMBERG</span><span>DRY</span><span>GIN</span></h1>
    <div class="mountains" role="img" aria-label="Bergpanorama in Grau und Anthrazit mit goldenen Blütenpollen"></div>
    <div class="brand-block">
      <div class="brand">SILVERKITE</div>
      <div class="brand-dot"></div>
      <div class="claim">
        <span>handcraftet</span><br>
        <span class="pollen">einzigartig mit blütenpollen</span>
        <span class="volume">500 ml &nbsp;.&nbsp; 45% Vol</span>
      </div>
    </div>
  </div>
</body>
</html>
```